TitleForge.com - Brandable Business Name Marketplace!

What is Title Forge?
Title Forge is a website that helps businesses build a name (or find a new name) for
their new product, service, or business. Over 2 million new businesses start each year,
and even more new products are created, and each one needs a unique name!
Other competitor branding sites for reference: www.MarkPail.com, www.Tagtastic.com, www.SignStem.com, www.markzo.com
What does Title Forge do?
Every business/product has a website, and the ‘address’ of the website is called
a ‘domain name’. We find valuable ‘domain names’ that are unique, catchy, or keyword-rich.
We then create a logo to capture the vision of the possibilities of that name. Then we write a
creative description of name, which further evolves the vision of the name.
We also help domain owners submit and sell their valuable digital real estate (domain).
How does the website function?
The ‘home’ page of the site should be modern, clean, and straight to the point (the
logos). The main focus is on the ‘logos’. There should be 5-6 logos per row and around
100 logos per page. The ‘description’ of each logo is NOT displayed UNTIL the visitor
clicks on a logo. Then the description, tags, category, and price will EXPAND ON SAME
PAGE (Not open in new page). Once the logo expands to reveal the description, tags,
category, and price, then the visitor can click on the name of the logo and THEN a
new page will open with options to add to cart or buy now.
What comes with each purchase?
1) Years of experience and expertise, ready to help builder your name!
2) Ownership of the valuable domain name, (digital real estate)
3) Custom logo artwork is included. And ideas for branding!
What happens after the customer completes purchase?
After completing our secure SSL checkout process, which accepts all major credit
cards and options for bank wire. The customer will be emailed transfer instructions.
The payment is held in escrow until the customer confirms delivery of the domain name.
Does title forge own all the names on the site?
Not all the names, some. Title forge allows owners of domain names to
‘Submit’ their domain names for acceptance to be listed on our site. After our team ‘reviews’
the names, they will be accepted or rejected. The domain names that are suitable
for our target audience, will be emailed with instructions to ‘forward’ the domain to
the Title Forge site. Once our system verifies the domain is correctly forwarded, the
domain owner will be emailed with instructions and listing fees to be paid.
What the site needs:
1) The site must have a login for domain owners. Each domain owner will have
an account profile where they can:
• a) submit their domain names to list on our site
• b) verify accepted names
• c) pay listing fees
• d) describe what the domain means to the owner
• e) adjust the price (we determine fair market value) by 20% up or down.
• f) profile page (portfolio of names)
2) The site must display the logo artwork as the main focus of the site.
3) The site must have a newsletter page.
4) The site must have an about us page.
5) The site must have contact page.
6) The site must have a FAQ page.
7) The site must have a ‘search bar’
8) The site must have a ’price range filter’ to sort names.
9) The site must have an option to sort names by: categories
10) The site must have an option to ‘rearrange’ the logos by:
• a) ’Date’
• b) ’Price’
• c) ’Alphabetical order’
• d) ’Staff picks’.
Summary:
We want to help businesses build a name for their product/service/company. The true value of what we sell is in the domain names, however the inspiration, possibilities, and vision is captured in the logos. The site will get tons of natural traffic because all the domain names listed on the site will be forwarded to TitleForge.com and we will actively advertise. Upon arrival the visitors will see catchy, unique, and keyword rich logos. Upon clicking on a logo, the logo will expand to display, description, category, price, and possible business uses. Upon clicking further, a new page will open (the landing page for each domain name if entered directly into browser) which will give options to inquire, add to cart, favorite, or buy now!. There will be a login for domain owners where they can submit new domain names, verify ownership by forwarding domain, pay listing fee, describe accepted name, and adjust our chosen price up or down by 20%. They will also have a profile page which will display only their portfolio of names with logos. There will be a Newsletter, FAQ, About Us, Contact, and Login Pages.
Target Market(s)
Business owners who want a brandable name for their business/service/product
Industry/Entity Type
Business
Number of Pages Required
1 page
Look and feel

```html
<!DOCTYPE html>
<html lang="en">
<head>
<meta charset="utf-8">
<title>Title Forge – Brandable Business Names</title>
<link href="https://fonts.googleapis.com/css2?family=Montserrat:wght@400;600;700&family=Open+Sans:wght@400;600;700&display=swap" rel="stylesheet">
<style>
:root{
  --page:#0c131c;
  --page-deep:#080d14;
  --hero-light:#5d7894;
  --hero-mid:#2c4560;
  --hero-dark:#142131;
  --white:#ffffff;
  --blue:#2b77cf;
  --blue-dark:#1f5fad;
  --tile-band:#d4dce5;
  --tile-tag:#c3ccd6;
  --tile-text:#333d48;
  --line:rgba(255,255,255,.55);
  --box:rgba(20,36,56,.72);
}
*{box-sizing:border-box;margin:0;padding:0}
html,body{width:767px;height:1200px;overflow:hidden;background:var(--page)}
body{font-family:"Open Sans",Arial,sans-serif;color:var(--white);position:relative}
.hero-photo{position:absolute;left:0;top:0;width:767px;height:560px;
  background:linear-gradient(180deg,var(--hero-light) 0%,var(--hero-mid) 30%,var(--hero-dark) 62%,var(--page) 100%),
  linear-gradient(90deg,rgba(255,255,255,.12),rgba(0,0,0,0) 60%);}
.main-nav{position:absolute;top:30px;left:136px;width:524px;height:28px;border-bottom:1px solid var(--line);display:flex;align-items:center}
.main-nav a{color:var(--white);text-decoration:none;font-size:10px;margin-right:0;position:absolute;top:4px}
.main-nav a.active{border-bottom:1px solid var(--white);padding-bottom:2px}
.login-btn{position:absolute;left:294px;top:2px;width:46px;height:18px;border-radius:9px;background:var(--blue);font-size:10px;display:flex;align-items:center;justify-content:center}
.search{position:absolute;left:344px;top:2px;width:103px;height:18px;border:1px solid var(--white);border-radius:9px;font-size:9px;padding-left:8px;display:flex;align-items:center}
.search svg{position:absolute;right:6px;top:4px}
.cart{position:absolute;left:456px;top:1px}
.cart-count{position:absolute;left:478px;top:3px;width:16px;height:16px;border-radius:50%;background:var(--white);color:var(--tile-text);font-size:9px;display:flex;align-items:center;justify-content:center}
.brand{position:absolute;top:128px;left:0;width:767px;text-align:center}
.brand-dot{display:block;width:26px;height:26px;border:3px solid var(--white);border-radius:50%;margin:0 auto 26px}
.brand-name{font-family:"Montserrat",sans-serif;font-weight:600;font-size:24px;letter-spacing:.5px}
.filters{position:absolute;top:280px;left:237px;height:22px;display:flex;gap:3px}
.pill{height:22px;border-radius:11px;font-size:8.5px;font-weight:600;display:flex;align-items:center;justify-content:center;color:var(--white)}
.pill.category{width:81px;border:1.5px solid var(--white)}
.pill.sort{width:60px;background:var(--blue)}
.pill.price{width:137px;background:var(--blue);justify-content:space-between;padding:0 14px;margin-left:8px}
.social{position:absolute;top:319px;left:333px;display:flex;gap:5px}
.social span{width:16px;height:16px;border-radius:50%;background:var(--white)}
.social span.on{background:var(--blue)}
.categories{position:absolute;top:414px;left:64px;display:flex;gap:21px}
.category-box{height:69px;border:2px solid var(--white);outline:4px solid rgba(255,255,255,.12);background:var(--box);font-family:"Montserrat",sans-serif;font-weight:600;font-size:17px;display:flex;align-items:center;justify-content:center}
.featured-title{position:absolute;top:533px;left:0;width:767px;text-align:center;font-family:"Montserrat",sans-serif;font-weight:600;font-size:12.5px}
.featured-title::after{content:"";display:block;width:90px;height:2px;background:var(--white);margin:6px auto 0}
.name-grid{position:absolute;top:580px;left:60px;display:grid;grid-template-columns:repeat(6,99px);column-gap:10.6px;row-gap:28px}
.name-tile{position:relative;width:99px;height:94px;background:var(--white);box-shadow:0 2px 6px rgba(0,0,0,.5)}
.price-tag{position:absolute;top:-7px;left:27px;width:50px;height:14px;background:var(--tile-tag);color:var(--tile-text);font-size:8px;display:flex;align-items:center;justify-content:center}
.name-mark{height:72px;display:flex;align-items:center;justify-content:center;gap:4px;font-family:"Montserrat",sans-serif;font-weight:600;font-size:14px}
.name-mark i{width:9px;height:9px;border-radius:50%;background:currentColor;display:inline-block}
.name-mark i.sq{border-radius:0}
.domain{height:22px;background:var(--tile-band);color:var(--tile-text);font-size:9px;display:flex;align-items:center;justify-content:center}
.name-tile.selected .price-tag,.name-tile.selected .domain{background:var(--blue);color:var(--white)}
.pager{position:absolute;top:1065px;left:245px;width:277px;height:21px;background:var(--blue-dark);border-radius:2px;display:flex;align-items:center;padding:0 9px;gap:4px}
.pager .dot{width:10px;height:10px;border-radius:50%;background:var(--white)}
.pager .num{width:12px;height:12px;border-radius:50%;background:var(--blue);border:1px solid var(--white);font-size:7px;display:flex;align-items:center;justify-content:center}
.pager .oval{width:16px;height:10px;border-radius:5px;background:var(--white)}
.pager .label{font-size:7px;width:22px;text-align:center}
.pager .gap{flex:1}
.site-footer{position:absolute;top:1140px;left:0;width:767px;height:60px;background:var(--page-deep);border-top:1px solid rgba(255,255,255,.08);font-size:9.5px}
.payments{position:absolute;left:60px;top:24px;display:flex;gap:3px}
.payments span{width:23px;height:15px;border-radius:2px;background:#c9d3de}
.payments span:nth-child(2){background:#e7e9ec}
.payments span:nth-child(3){background:#dfe6f3}
.payments span:nth-child(4){background:#8fb4df}
.copyright{position:absolute;left:252px;top:26px}
.copyright .tos{color:#6ea8ff;text-decoration:underline}
.phone{position:absolute;left:531px;top:26px}
</style>
</head>
<body>
<div class="hero-photo" role="img" aria-label="Photo of two businessmen in suits reviewing documents at an office desk"></div>

<nav class="main-nav">
  <a class="active" style="left:0">Home</a>
  <a style="left:46px">Shop</a>
  <a style="left:88px">About Us</a>
  <a style="left:149px">Help</a>
  <a style="left:190px">Cart</a>
  <a style="left:228px">News Letter</a>
  <span class="login-btn">Login</span>
  <span class="search">Search
    <svg width="9" height="9" viewBox="0 0 10 10"><circle cx="4" cy="4" r="3" fill="none" stroke="#fff" stroke-width="1.3"/><line x1="6.3" y1="6.3" x2="9.2" y2="9.2" stroke="#fff" stroke-width="1.4"/></svg>
  </span>
  <svg class="cart" width="20" height="18" viewBox="0 0 20 18"><path d="M1 2h3l2.5 9h9l2.5-7H5" fill="none" stroke="#fff" stroke-width="1.6"/><circle cx="8" cy="15" r="1.6" fill="#fff"/><circle cx="15" cy="15" r="1.6" fill="#fff"/></svg>
  <span class="cart-count">0</span>
</nav>

<header class="brand">
  <span class="brand-dot"></span>
  <div class="brand-name">Title Forge</div>
</header>

<div class="filters">
  <span class="pill category">Category</span>
  <span class="pill sort">Sort By</span>
  <span class="pill price"><b>$</b>Filter Price<b>$</b></span>
</div>

<div class="social" aria-label="Social links"><span></span><span class="on"></span><span></span><span></span><span></span></div>

<div class="categories">
  <div class="category-box" style="width:200px">INVENTED NAMES</div>
  <div class="category-box" style="width:195px">KEYWORD NAMES</div>
  <div class="category-box" style="width:199px">NEW EXTENSIONS</div>
</div>

<h2 class="featured-title">FEATURED NAMES</h2>

<main class="name-grid">
  <div class="name-tile selected"><span class="price-tag">$3,295</span><div class="name-mark" style="color:#8a8f94">Gearlify</div><div class="domain">gearlify.com</div></div>
  <div class="name-tile"><span class="price-tag">$3,295</span><div class="name-mark" style="color:#2aa3e0">Dewcrate</div><div class="domain">dewcrate.com</div></div>
  <div class="name-tile"><span class="price-tag">$3,295</span><div class="name-mark" style="color:#e2542c"><i class="sq"></i>glowvex</div><div class="domain">glowvex.com</div></div>
  <div class="name-tile"><span class="price-tag">$3,295</span><div class="name-mark" style="color:#d8312b;font-size:12px">GUIDENEST</div><div class="domain">guidenest.com</div></div>
  <div class="name-tile"><span class="price-tag">$3,295</span><div class="name-mark" style="color:#1f5ea8"><i></i>velmira</div><div class="domain">velmira.com</div></div>
  <div class="name-tile"><span class="price-tag">$3,295</span><div class="name-mark" style="color:#2b78c2;font-size:12.5px">nestbreeze</div><div class="domain">nestbreeze.com</div></div>

  <div class="name-tile"><span class="price-tag">$3,295</span><div class="name-mark" style="color:#6d8f1f">ofolof</div><div class="domain">ofolof.com</div></div>
  <div class="name-tile"><span class="price-tag">$3,295</span><div class="name-mark" style="color:#8e3a8c">Blendora</div><div class="domain">blendora.com</div></div>
  <div class="name-tile"><span class="price-tag">$3,295</span><div class="name-mark" style="color:#2b3f8f">TONVARO</div><div class="domain">tonvaro.com</div></div>
  <div class="name-tile"><span class="price-tag">$3,295</span><div class="name-mark" style="color:#1c4a8c"><i class="sq"></i>wavelux</div><div class="domain">wavelux.com</div></div>
  <div class="name-tile"><span class="price-tag">$3,295</span><div class="name-mark" style="color:#3a3f8a">Kinetra</div><div class="domain">kinetra.com</div></div>
  <div class="name-tile"><span class="price-tag">$3,295</span><div class="name-mark" style="color:#3b3f8e;font-size:12px">PILEGROVE</div><div class="domain">pilegrove.com</div></div>

  <div class="name-tile"><span class="price-tag">$3,295</span><div class="name-mark" style="color:#e0782a"><i></i>voltrix</div><div class="domain">voltrix.com</div></div>
  <div class="name-tile"><span class="price-tag">$3,295</span><div class="name-mark" style="color:#3c4450">ARCHVIO</div><div class="domain">archvio.com</div></div>
  <div class="name-tile"><span class="price-tag">$3,295</span><div class="name-mark" style="color:#1d4f7a">launchiq</div><div class="domain">launchiq.com</div></div>
  <div class="name-tile"><span class="price-tag">$3,295</span><div class="name-mark" style="color:#b8321c">Hummatic</div><div class="domain">hummatic.com</div></div>
  <div class="name-tile"><span class="price-tag">$3,295</span><div class="name-mark" style="color:#2f8a3a"><i class="sq"></i>datumly</div><div class="domain">datumly.com</div></div>
  <div class="name-tile"><span class="price-tag">$3,295</span><div class="name-mark" style="color:#2f3540"><i></i>pirella</div><div class="domain">pirella.com</div></div>

  <div class="name-tile"><span class="price-tag">$3,295</span><div class="name-mark" style="color:#e0782a"><i></i>voltrix</div><div class="domain">voltrix.com</div></div>
  <div class="name-tile"><span class="price-tag">$3,295</span><div class="name-mark" style="color:#3c4450">ARCHVIO</div><div class="domain">archvio.com</div></div>
  <div class="name-tile"><span class="price-tag">$3,295</span><div class="name-mark" style="color:#1d4f7a">launchiq</div><div class="domain">launchiq.com</div></div>
  <div class="name-tile"><span class="price-tag">$3,295</span><div class="name-mark" style="color:#b8321c">Hummatic</div><div class="domain">hummatic.com</div></div>
  <div class="name-tile"><span class="price-tag">$3,295</span><div class="name-mark" style="color:#2f8a3a"><i class="sq"></i>datumly</div><div class="domain">datumly.com</div></div>
  <div class="name-tile"><span class="price-tag">$3,295</span><div class="name-mark" style="color:#2f3540"><i></i>pirella</div><div class="domain">pirella.com</div></div>
</main>

<div class="pager">
  <svg width="8" height="10" viewBox="0 0 8 10"><path d="M6 1L2 5l4 4" fill="none" stroke="#fff" stroke-width="1.6"/></svg>
  <span class="gap"></span>
  <span class="num">1</span>
  <span class="dot"></span><span class="dot"></span><span class="dot"></span><span class="dot"></span>
  <span class="dot"></span><span class="dot"></span><span class="dot"></span><span class="dot"></span>
  <span class="oval"></span><span class="label">100</span><span class="oval"></span>
  <span class="gap"></span>
  <svg width="8" height="10" viewBox="0 0 8 10"><path d="M2 1l4 4-4 4" fill="none" stroke="#fff" stroke-width="1.6"/></svg>
</div>

<footer class="site-footer">
  <div class="payments" aria-label="Accepted payment methods"><span></span><span></span><span></span><span></span></div>
  <div class="copyright">© 2015 Title Forge .  All Reserved  /  <span class="tos">TOS</span>  /  Privacy Policy</div>
  <div class="phone">1 - 800 - 000 - 0000</div>
</footer>
</body>
</html>
```